Social responsible Renewable Energy company

We at voltaQ are an independent power producer company founded in 2021 that handles large scale deployment of Renewable Energy and carbon neutral Energy as a service model. We offer turnkey solutions using solar panel systems and this could be incorporated in our business cards. You can also find our logo in the documents provided. Another key issue is that the business cards will be printed on recicled paper, not sure if this is a limitation in deciding the design. The recycled sign should also be added on the business card and stating that the paper used was recycled. Our website is www.myvoltaq.example. It should also be very professional, not too dreamy but still needs to capture your imagination. We are really excited to get your ideas !

Target Market(s)

Renewable Energy market

Contact Information for Business Card

The business card will be printed on recycled paper. Name of the company is voltaQ. Website is www.myvoltaq.example

Requirements
Nice to have
• Our motto: Powered by renewable, driven by people.

```html
<!DOCTYPE html>
<html lang="en">
<head>
<meta charset="utf-8">
<title>voltaQ business card</title>
<link href="https://fonts.googleapis.com/css2?family=Montserrat:wght@400;500;600;700&display=swap" rel="stylesheet">
<style>
  :root {
    --backdrop: #5d7287;
    --navy: #1d4a78;
    --sky: #3a8fd6;
    --paper: #f5f5f4;
    --blue-deep: #1d5e96;
    --blue-bright: #2b86cb;
    --white: #ffffff;
    --sun-warm: #f0a45a;
    --sun-light: #f6dcae;
    --sun-dusk: #b9687a;
  }
  * { margin: 0; padding: 0; box-sizing: border-box; }
  html, body {
    width: 1200px; height: 801px; overflow: hidden;
    background: var(--backdrop);
    font-family: "Montserrat", sans-serif;
  }
  .stage {
    position: relative; width: 1200px; height: 801px;
  }
  .card {
    position: absolute;
    width: 540px; height: 309px;
    border-radius: 3px;
    overflow: hidden;
    box-shadow: 0 18px 40px rgba(20, 35, 50, 0.35);
  }
  /* Front */
  .card-front { left: 40px; top: 246px; background: var(--paper); display: flex; }
  .front-photo {
    position: relative;
    width: 272px; height: 100%;
    background:
      radial-gradient(circle at 52% 50%, var(--sun-light) 0 12%, var(--sun-warm) 28%, transparent 55%),
      linear-gradient(160deg, var(--sun-light) 0%, var(--sun-warm) 45%, var(--sun-dusk) 100%);
  }
  .cert-badge {
    position: absolute; left: 16px; bottom: 16px;
    width: 26px; height: 26px; border-radius: 50%;
    border: 2px solid var(--white);
  }
  .front-details {
    flex: 1;
    padding: 30px 28px 24px 20px;
    text-align: right;
    color: var(--navy);
  }
  .brand-name {
    display: flex; justify-content: flex-end; align-items: center; gap: 10px;
    font-size: 42px; font-weight: 600; letter-spacing: -0.5px;
    color: var(--navy);
    line-height: 1;
  }
  .brand-dot { width: 14px; height: 14px; border-radius: 50%; background: var(--sky); }
  .person-name {
    margin-top: 26px;
    font-size: 17px; font-weight: 600; letter-spacing: 3.5px;
  }
  .person-role {
    font-size: 15px; font-weight: 500; color: var(--sky); margin-top: 1px;
  }
  .contact-list { list-style: none; margin-top: 12px; font-size: 11.5px; line-height: 1.55; }
  .contact-list li { display: flex; justify-content: flex-end; align-items: center; gap: 6px; }
  .contact-list svg { width: 9px; height: 9px; fill: var(--sky); flex: none; }
  .offer {
    margin-top: 10px;
    font-size: 11.5px; font-weight: 700; line-height: 1.25;
  }
  /* Back */
  .card-back {
    left: 620px; top: 246px;
    background: linear-gradient(200deg, var(--blue-deep) 0%, var(--blue-bright) 100%);
    color: var(--white);
  }
  .back-brand {
    position: absolute; left: 0; right: 0; top: 96px;
    display: flex; justify-content: center; align-items: center; gap: 14px;
    font-size: 76px; font-weight: 600; letter-spacing: -1px; line-height: 1;
  }
  .back-brand .brand-dot { width: 22px; height: 22px; background: var(--white); }
  .motto {
    position: absolute; left: 40px; right: 40px; bottom: 34px;
    font-size: 13px; font-weight: 600; letter-spacing: 3.2px;
    text-align: center;
  }
</style>
</head>
<body>
<main class="stage">
  <section class="card card-front">
    <div class="front-photo" role="img" aria-label="Photo of hands framing the setting sun in warm orange light">
      <span class="cert-badge" role="img" aria-label="Recycled paper certification badge"></span>
    </div>
    <div class="front-details">
      <div class="brand-name">voltaQ<span class="brand-dot"></span></div>
      <h1 class="person-name">LOREM IPSUM</h1>
      <p class="person-role">Founder</p>
      <ul class="contact-list">
        <li>000 000 0000
          <svg viewBox="0 0 10 10" aria-hidden="true"><path d="M2 0.5 L3.8 2.6 L2.9 3.8 Q4 6 6.2 7.1 L7.4 6.2 L9.5 8 L8.2 9.5 Q1 8.5 0.5 1.8 Z"/></svg>
        </li>
        <li>loremipsum@myvoltaq.example
          <svg viewBox="0 0 10 10" aria-hidden="true"><path d="M0 2 H10 V8.5 H0 Z M0.6 2.4 L5 5.8 L9.4 2.4" stroke="#fff" stroke-width="0.8"/></svg>
        </li>
        <li>www.myvoltaq.example
          <svg viewBox="0 0 10 10" aria-hidden="true"><circle cx="5" cy="5" r="4.6"/><path d="M0.6 5 H9.4 M5 0.5 V9.5 M5 0.5 Q2 5 5 9.5 M5 0.5 Q8 5 5 9.5" stroke="#fff" stroke-width="0.6" fill="none"/></svg>
        </li>
      </ul>
      <p class="offer">We offer turnkey solutions using<br>solar panel systems</p>
    </div>
  </section>

  <section class="card card-back">
    <div class="back-brand">voltaQ<span class="brand-dot"></span></div>
    <p class="motto">POWERED BY RENEWABLE, DRIVEN BY PEOPLE</p>
  </section>
</main>
</body>
</html>
```